Lien Post Card - (5.5 x 8.5)

FRONT OF POSTCARD
Is a Property Lien Putting Your Home at Risk?
HOA Liens • Tax Liens • Municipal Charges • Other Property-Related Liens
You may have options to resolve outstanding liens and protect your home.
A Refinance or Home Equity Line of Credit (HELOC) may help you:
✔ Pay off qualifying liens
✔ Consolidate debt into one manageable payment
✔ Access your home's equity
✔ Improve your financial flexibility
✔ Avoid additional penalties, fees, or collection actions
Don't wait until the situation becomes more difficult.
Call today for a confidential review of your options.
Bluegate Lending Partners, Inc.
(800) 647-2915 x 42
www.bluegatelendco.com
NMLS #381640
BACK OF POSTCARD
Your Home Equity Could Be the Solution
If you have received notices regarding:
• Delinquent Property Taxes
• HOA or Condo Association Assessments
• Municipal Utility Liens
• Special Assessments
• Other Property-Related Obligations
You may qualify for financing options designed to help satisfy those obligations and bring your property current.
Our experienced mortgage professionals can review your situation and discuss available programs, including:
• Cash-Out Refinancing
• Home Equity Lines of Credit (HELOCs)
• Home Equity Loans
• Debt Consolidation Solutions
Free Consultation • No Obligation
Contact Marcus Delaney today at (800) 647-2915 x42 or mdelaney@bluegatelendco.com (NMLS #57308)

```html
<!DOCTYPE html>
<html lang="en">
<head>
<meta charset="utf-8">
<title>Lien Postcard – Bluegate Lending Partners</title>
<link href="https://fonts.googleapis.com/css2?family=Montserrat:wght@400;500;600;700;800&display=swap" rel="stylesheet">
<style>
:root{
  --sheet:#e9eaec;
  --navy:#0e1822;
  --white:#ffffff;
  --text-soft:#e3e8ef;
  --gold:#f1c063;
  --blue-1:#3f63a8;
  --blue-2:#7b9bd6;
  --ink:#13202c;
  --line:#333;
}
*{box-sizing:border-box;margin:0;padding:0}
html,body{width:1200px;height:416px;overflow:hidden;background:var(--sheet);font-family:"Montserrat",sans-serif}
.card{position:absolute;top:17px;width:578px;height:381px;overflow:hidden;box-shadow:0 2px 6px rgba(0,0,0,.25)}
.front{left:18px;background:var(--navy)}
.back{left:604px;background:var(--white)}
.abs{position:absolute}

/* front */
.skyline{left:170px;top:0;width:408px;height:230px;
  background:radial-gradient(ellipse 120px 80px at 280px 150px,rgba(240,150,60,.85),rgba(150,80,40,.45) 45%,transparent 80%),
  linear-gradient(180deg,#3a4450 0%,#2a2e34 40%,#1a2028 75%,var(--navy) 100%);
  -webkit-mask:linear-gradient(90deg,transparent 0,#000 30%);mask:linear-gradient(90deg,transparent 0,#000 30%)}
.brand{left:20px;top:30px;display:flex;align-items:center;gap:7px;color:var(--gold);font-weight:700;font-size:12px;line-height:1.15;width:150px}
.brand-mark{width:14px;height:14px;border-radius:50%;background:var(--gold);flex:none}
.headline{left:18px;top:120px;color:var(--white);font-weight:600;font-size:23.5px;line-height:1.15;width:260px}
.lien-pill{left:17px;top:215px;width:231px;height:33px;background:linear-gradient(90deg,var(--gold),#f4cf7e);border-radius:0 9px 9px 0;color:var(--ink);font-size:9.6px;font-weight:500;padding:4px 0 0 10px;line-height:1.3}
.options{left:18px;top:270px;color:var(--white);font-size:12.8px;font-weight:500;line-height:1.55;width:290px}
.benefits-title{left:314px;top:166px;color:var(--white);font-size:12.4px;font-weight:500;line-height:1.5}
.checklist{left:314px;top:215px;list-style:none;color:var(--text-soft);font-size:9.4px;line-height:18.4px}
.checklist li,.back-list li{display:flex;align-items:center;gap:6px}
.tick{width:9px;height:9px;flex:none}
.cta-band{left:0;top:316px;width:578px;height:65px;background:linear-gradient(90deg,var(--blue-1),var(--blue-2))}
.dont-wait{left:17px;top:328px;color:var(--white);font-size:11px;line-height:1.35;width:160px}
.dont-wait b{font-weight:800}
.call-box{left:179px;top:316px;width:231px;height:65px;background:var(--gold);border-radius:22px 0 0 0;padding:11px 0 0 72px;color:var(--ink)}
.call-box p{font-size:9.6px;line-height:1.3}
.call-box p b{font-weight:700}
.call-box .phone-num{font-size:12px;font-weight:700;margin-top:4px}
.phone-dot{position:absolute;left:22px;top:15px;width:36px;height:36px;border-radius:50%;background:var(--ink);display:flex;align-items:center;justify-content:center}
.contact{left:418px;top:327px;color:var(--white);font-size:8.6px;line-height:15px}
.contact div{display:flex;align-items:center;gap:5px}
.contact .plain{padding-left:14px}

/* back */
.info-panel{left:0;top:0;width:289px;height:381px;background:var(--navy);border-radius:0 34px 0 0}
.back-title{left:16px;top:18px;color:var(--white);font-size:11.4px;font-weight:700;white-space:nowrap}
.back-sub{left:16px;top:34px;color:var(--white);font-size:10.2px;font-weight:500}
.back-list{list-style:none;color:var(--text-soft);font-size:9.2px;line-height:18.5px}
.list-a{left:16px;top:55px}
.list-b{left:16px;top:222px}
.back-copy{left:16px;color:var(--text-soft);font-size:8.9px;line-height:14px;width:262px}
.copy-1{top:152px}
.copy-2{top:187px;font-weight:700;color:var(--white)}
.agent-band{left:0;top:312px;width:289px;height:69px;background:linear-gradient(90deg,var(--blue-1),var(--blue-2))}
.agent-photo{left:14px;top:298px;width:68px;height:68px;border-radius:50%;background:linear-gradient(160deg,#5a6270,#20262e);border:2px solid #8fa9d8}
.agent{left:84px;top:338px;color:var(--white);font-size:9.4px;font-weight:600;line-height:14px;white-space:nowrap}
.agent-web{left:184px;top:338px;color:var(--white);font-size:7.6px;font-weight:600;line-height:14px;white-space:nowrap}
.badge{left:198px;top:244px;width:88px;height:84px}
.badge-text{position:absolute;inset:0;display:flex;flex-direction:column;align-items:center;justify-content:center;color:var(--ink);font-weight:800;line-height:1.1;text-align:center}
.badge-text .big{font-size:11px}
.badge-text .small{font-size:6.6px}
.stamp{left:512px;top:18px;width:51px;height:51px;border:1px solid var(--line)}
.address-box{left:305px;top:233px;width:232px;height:99px;border:1px solid var(--line)}
</style>
</head>
<body>

<section class="card front" aria-label="Postcard front">
  <div class="abs skyline" role="img" aria-label="City skyline silhouetted against a sunset sky"></div>
  <div class="abs brand"><span class="brand-mark"></span>Bluegate Lending Partners</div>
  <h1 class="abs headline">Is a Property Lien Putting Your Home at Risk?</h1>
  <div class="abs lien-pill">• HOA Liens • Tax Liens • Municipal Charges<br>• Other Property-Related Liens</div>
  <p class="abs options">You may have options to resolve outstanding liens and protect your home.</p>
  <h2 class="abs benefits-title">A Refinance or Home Equity Line<br>of Credit (HELOC) may help you:</h2>
  <ul class="abs checklist">
    <li><svg class="tick" viewBox="0 0 10 10"><path d="M1 5.5l2.5 2.5L9 1.5" fill="none" stroke="#f1c063" stroke-width="1.8"/></svg>Pay off qualifying liens</li>
    <li><svg class="tick" viewBox="0 0 10 10"><path d="M1 5.5l2.5 2.5L9 1.5" fill="none" stroke="#f1c063" stroke-width="1.8"/></svg>Consolidate debt into one manageable payment</li>
    <li><svg class="tick" viewBox="0 0 10 10"><path d="M1 5.5l2.5 2.5L9 1.5" fill="none" stroke="#f1c063" stroke-width="1.8"/></svg>Access your home's equity</li>
    <li><svg class="tick" viewBox="0 0 10 10"><path d="M1 5.5l2.5 2.5L9 1.5" fill="none" stroke="#f1c063" stroke-width="1.8"/></svg>Improve your financial flexibility</li>
    <li><svg class="tick" viewBox="0 0 10 10"><path d="M1 5.5l2.5 2.5L9 1.5" fill="none" stroke="#f1c063" stroke-width="1.8"/></svg>Avoid additional penalties, fees, or collection actions</li>
  </ul>
  <div class="abs cta-band"></div>
  <p class="abs dont-wait"><b>DON'T WAIT</b> until the situation becomes more difficult.</p>
  <div class="abs call-box">
    <span class="phone-dot"><svg width="16" height="16" viewBox="0 0 24 24"><path fill="#fff" d="M6.6 10.8a15.1 15.1 0 0 0 6.6 6.6l2.2-2.2c.3-.3.7-.4 1-.2 1.1.4 2.3.6 3.6.6.6 0 1 .4 1 1V20c0 .6-.4 1-1 1A17 17 0 0 1 3 4c0-.6.4-1 1-1h3.5c.6 0 1 .4 1 1 0 1.3.2 2.5.6 3.6.1.3 0 .7-.2 1z"/></svg></span>
    <p><b>Call today</b> for a confidential<br>review of your options.</p>
    <p class="phone-num">(800) 647-2915 x 42</p>
  </div>
  <div class="abs contact">
    <div><svg width="9" height="11" viewBox="0 0 10 12"><path fill="#fff" d="M5 0a4 4 0 0 0-4 4c0 3 4 8 4 8s4-5 4-8a4 4 0 0 0-4-4zm0 5.5A1.5 1.5 0 1 1 5 2.5a1.5 1.5 0 0 1 0 3z"/></svg>Bluegate Lending Partners, Inc.</div>
    <div><svg width="9" height="9" viewBox="0 0 10 10"><circle cx="5" cy="5" r="4.3" fill="none" stroke="#fff"/><path d="M.7 5h8.6M5 .7c-2.4 2.6-2.4 6 0 8.6M5 .7c2.4 2.6 2.4 6 0 8.6" fill="none" stroke="#fff" stroke-width=".8"/></svg>www.bluegatelendco.com</div>
    <div class="plain">NMLS #381640</div>
  </div>
</section>

<section class="card back" aria-label="Postcard back">
  <div class="abs info-panel"></div>
  <h2 class="abs back-title">Your Home Equity Could Be the Solution</h2>
  <p class="abs back-sub">If you have received notices regarding:</p>
  <ul class="abs back-list list-a">
    <li><svg class="tick" viewBox="0 0 10 10"><path d="M1 5.5l2.5 2.5L9 1.5" fill="none" stroke="#f1c063" stroke-width="1.8"/></svg>Delinquent Property Taxes</li>
    <li><svg class="tick" viewBox="0 0 10 10"><path d="M1 5.5l2.5 2.5L9 1.5" fill="none" stroke="#f1c063" stroke-width="1.8"/></svg>HOA or Condo Association Assessments</li>
    <li><svg class="tick" viewBox="0 0 10 10"><path d="M1 5.5l2.5 2.5L9 1.5" fill="none" stroke="#f1c063" stroke-width="1.8"/></svg>Municipal Utility Liens</li>
    <li><svg class="tick" viewBox="0 0 10 10"><path d="M1 5.5l2.5 2.5L9 1.5" fill="none" stroke="#f1c063" stroke-width="1.8"/></svg>Special Assessments</li>
    <li><svg class="tick" viewBox="0 0 10 10"><path d="M1 5.5l2.5 2.5L9 1.5" fill="none" stroke="#f1c063" stroke-width="1.8"/></svg>Other Property-Related Obligations</li>
  </ul>
  <p class="abs back-copy copy-1">You may qualify for financing options designed to help satisfy those obligations and bring your property current.</p>
  <p class="abs back-copy copy-2">Our experienced mortgage professionals can review your situation and discuss available programs, including:</p>
  <ul class="abs back-list list-b">
    <li><svg class="tick" viewBox="0 0 10 10"><path d="M1 5.5l2.5 2.5L9 1.5" fill="none" stroke="#f1c063" stroke-width="1.8"/></svg>Cash-Out Refinancing</li>
    <li><svg class="tick" viewBox="0 0 10 10"><path d="M1 5.5l2.5 2.5L9 1.5" fill="none" stroke="#f1c063" stroke-width="1.8"/></svg>Home Equity Lines of Credit (HELOCs)</li>
    <li><svg class="tick" viewBox="0 0 10 10"><path d="M1 5.5l2.5 2.5L9 1.5" fill="none" stroke="#f1c063" stroke-width="1.8"/></svg>Home Equity Loans</li>
    <li><svg class="tick" viewBox="0 0 10 10"><path d="M1 5.5l2.5 2.5L9 1.5" fill="none" stroke="#f1c063" stroke-width="1.8"/></svg>Debt Consolidation Solutions</li>
  </ul>
  <div class="abs agent-band"></div>
  <div class="abs agent-photo" role="img" aria-label="Portrait of the loan officer"></div>
  <p class="abs agent">Marcus Delaney<br>(800) 647-2915 x42</p>
  <p class="abs agent-web">www.bluegatelendco.com<br>(NMLS #381640)</p>
  <div class="abs badge">
    <svg width="88" height="84" viewBox="0 0 88 84"><polygon fill="#f1c063" points="44,0 51,10 62,4 64,16 76,15 72,27 84,31 75,40 84,49 72,54 76,66 64,65 62,77 51,71 44,84 37,71 26,77 24,65 12,66 16,54 4,49 13,40 4,31 16,27 12,15 24,16 26,4 37,10"/></svg>
    <div class="badge-text"><span class="big">FREE</span><span class="small">CONSULTATION</span><span class="big">NO</span><span class="small">OBLIGATION</span></div>
  </div>
  <div class="abs stamp"></div>
  <div class="abs address-box"></div>
</section>

</body>
</html>
```